Building and constructions

Extension, additions, alterations, renovations, new homes, project management and supervision

Industry/Entity Type

Building

Contact Information for Business Card

Morlaven building service constructions PTY LTD
Colin Marsh builder/ supervisor
BLD 71940 member of HTU
0411273509 email cmarsh71@qelmoranet.com

```html
<!DOCTYPE html>
<html lang="en">
<head>
<meta charset="utf-8">
<title>Morlaven Business Card</title>
<link href="https://fonts.googleapis.com/css2?family=Questrial&display=swap" rel="stylesheet">
<style>
  :root {
    --page: #ecebe8;
    --card-light: #ffffff;
    --card-dark: #3c3d3f;
    --ink-grey: #8a8b8d;
    --ink-light: #d9d9da;
    --accent: #f08a1c;
  }
  * { margin: 0; padding: 0; box-sizing: border-box; }
  html, body { width: 720px; height: 1200px; overflow: hidden; }
  body {
    background: var(--page);
    font-family: "Questrial", "Century Gothic", sans-serif;
    display: flex;
    flex-direction: column;
    align-items: center;
    justify-content: center;
    gap: 110px;
  }
  .card {
    position: relative;
    width: 600px;
    height: 343px;
    border-radius: 4px;
    box-shadow: 0 6px 18px rgba(0,0,0,0.18);
    overflow: hidden;
  }
  .card--front { background: var(--card-light); }
  .card--back  { background: var(--card-dark); }

  .brand { position: absolute; }
  .brand__row { display: flex; align-items: center; gap: 10px; }
  .brand__square { width: 30px; height: 30px; background: var(--accent); }
  .brand__name {
    font-size: 40px;
    letter-spacing: 9px;
    line-height: 1;
  }
  .brand__tagline {
    margin-top: 6px;
    margin-left: 40px;
    font-size: 9.5px;
    letter-spacing: 0.6px;
    text-transform: uppercase;
    color: var(--accent);
  }
  .card--front .brand { top: 56px; left: 250px; }
  .card--front .brand__name { color: var(--ink-grey); }
  .card--back .brand { top: 60px; left: 270px; }
  .card--back .brand__name { color: var(--ink-light); }

  .person { position: absolute; left: 42px; bottom: 40px; }
  .person__name { font-size: 26px; color: var(--ink-grey); }
  .person__role { font-size: 17px; color: var(--accent); margin-top: 2px; letter-spacing: 0.5px; }
  .person__licence { font-size: 13px; color: var(--accent); margin-top: 3px; }
  .contact { list-style: none; margin-top: 22px; }
  .contact__item {
    display: flex; align-items: center; gap: 10px;
    font-size: 14px; color: var(--ink-grey); margin-top: 8px;
  }
  .contact__icon { width: 13px; height: 13px; flex: none; }

  .services { position: absolute; left: 42px; bottom: 34px; list-style: none; }
  .services__item {
    display: flex; align-items: center; gap: 9px;
    font-size: 17px; color: var(--ink-light); margin-top: 9px;
  }
  .services__tick { width: 14px; height: 14px; flex: none; }
</style>
</head>
<body>

<section class="card card--front" aria-label="Business card front">
  <div class="brand">
    <div class="brand__row">
      <span class="brand__square"></span>
      <span class="brand__name">MORLAVEN</span>
    </div>
    <div class="brand__tagline">Building service constructions pty ltd</div>
  </div>

  <div class="person">
    <div class="person__name">Colin Marsh</div>
    <div class="person__role">Supervisor</div>
    <div class="person__licence">BLD 71940 member of HTU</div>
    <ul class="contact">
      <li class="contact__item">
        <svg class="contact__icon" viewBox="0 0 14 14" aria-hidden="true">
          <rect x="1" y="5" width="12" height="8" rx="1.5" fill="#f08a1c"/>
          <path d="M1 5 Q7 -1 13 5" fill="none" stroke="#f08a1c" stroke-width="2"/>
          <circle cx="7" cy="9" r="2" fill="#fff"/>
        </svg>
        0411273509
      </li>
      <li class="contact__item">
        <svg class="contact__icon" viewBox="0 0 14 14" aria-hidden="true">
          <rect x="0.5" y="2.5" width="13" height="9" fill="#f08a1c"/>
          <path d="M0.5 2.5 L7 8 L13.5 2.5" fill="none" stroke="#fff" stroke-width="1.2"/>
        </svg>
        cmarsh71@qelmoranet.com
      </li>
    </ul>
  </div>
</section>

<section class="card card--back" aria-label="Business card back">
  <div class="brand">
    <div class="brand__row">
      <span class="brand__square"></span>
      <span class="brand__name">MORLAVEN</span>
    </div>
    <div class="brand__tagline">Building service constructions pty ltd</div>
  </div>

  <ul class="services">
    <li class="services__item"><svg class="services__tick" viewBox="0 0 14 14" aria-hidden="true"><path d="M2 7.5 L5.5 11 L12 3" fill="none" stroke="#f08a1c" stroke-width="2.4"/></svg>Extension</li>
    <li class="services__item"><svg class="services__tick" viewBox="0 0 14 14" aria-hidden="true"><path d="M2 7.5 L5.5 11 L12 3" fill="none" stroke="#f08a1c" stroke-width="2.4"/></svg>Additions</li>
    <li class="services__item"><svg class="services__tick" viewBox="0 0 14 14" aria-hidden="true"><path d="M2 7.5 L5.5 11 L12 3" fill="none" stroke="#f08a1c" stroke-width="2.4"/></svg>Alterations</li>
    <li class="services__item"><svg class="services__tick" viewBox="0 0 14 14" aria-hidden="true"><path d="M2 7.5 L5.5 11 L12 3" fill="none" stroke="#f08a1c" stroke-width="2.4"/></svg>Renovations</li>
    <li class="services__item"><svg class="services__tick" viewBox="0 0 14 14" aria-hidden="true"><path d="M2 7.5 L5.5 11 L12 3" fill="none" stroke="#f08a1c" stroke-width="2.4"/></svg>New homes</li>
    <li class="services__item"><svg class="services__tick" viewBox="0 0 14 14" aria-hidden="true"><path d="M2 7.5 L5.5 11 L12 3" fill="none" stroke="#f08a1c" stroke-width="2.4"/></svg>Project management</li>
    <li class="services__item"><svg class="services__tick" viewBox="0 0 14 14" aria-hidden="true"><path d="M2 7.5 L5.5 11 L12 3" fill="none" stroke="#f08a1c" stroke-width="2.4"/></svg>supervision</li>
  </ul>
</section>

</body>
</html>
```